Law Offices business card

Hi there, I'll need business card for the Law Offices of Tobin Haskell. The information must convey his strategic approach and quick resolution to complex business litigation needs. Please emphasize Civil Litigation, Corporate Law, Business Governance and Real Estate Law. Tobin has over 25 years of experience in these fields.The card should be modern and edgy and the message should be clear. Please consult his current website for ideas.

Business

```html
<!DOCTYPE html>
<html lang="en">
<head>
<meta charset="utf-8">
<title>Law Offices of Tobin Haskell – Business Card</title>
<link href="https://fonts.googleapis.com/css2?family=Open+Sans:wght@400;600&display=swap" rel="stylesheet">
<style>
  :root {
    --backdrop: #e6e4e1;
    --charcoal: #3a3a3a;
    --charcoal-soft: #474747;
    --accent-yellow: #f1d038;
    --paper: #f6f6f6;
    --ink: #555555;
    --mark-grey: #d2d2d2;
    --white: #ffffff;
    --muted-white: #bdbdbd;
  }
  * { margin: 0; padding: 0; box-sizing: border-box; }
  html, body {
    width: 1200px; height: 1200px; overflow: hidden;
    background: var(--backdrop);
    font-family: "Open Sans", Arial, sans-serif;
  }
  .card {
    position: absolute; left: 240px; width: 720px; height: 433px;
    overflow: hidden;
    box-shadow: 0 4px 10px rgba(0,0,0,0.18);
  }
  .card-front { top: 117px; background: var(--charcoal); }
  .card-back { top: 615px; background: var(--paper); }
  .card-shapes { position: absolute; inset: 0; }

  .brand {
    position: absolute; display: flex; align-items: center; gap: 14px;
    text-transform: uppercase; white-space: nowrap;
  }
  .brand-dot { border-radius: 50%; flex: none; }
  .brand-front { left: 78px; top: 196px; }
  .brand-front .brand-dot { width: 32px; height: 32px; background: var(--white); }
  .brand-front .brand-name {
    color: var(--white); font-size: 27px; font-weight: 400; letter-spacing: 4px;
  }
  .practice {
    position: absolute; left: 124px; top: 248px; list-style: none;
    color: var(--muted-white); font-size: 10.5px; letter-spacing: 1.8px;
    line-height: 18px; text-transform: uppercase; white-space: nowrap;
  }
  .practice-years { color: var(--accent-yellow); margin-top: 6px; }

  .brand-back { left: 404px; top: 196px; }
  .brand-back .brand-dot { width: 26px; height: 26px; background: var(--mark-grey); }
  .brand-back .brand-name {
    color: var(--mark-grey); font-size: 21px; font-weight: 400; letter-spacing: 3px;
  }

  .holder { position: absolute; right: 346px; top: 20px; text-align: right; color: var(--white); }
  .holder-name { font-size: 22px; font-weight: 400; letter-spacing: 3.5px; line-height: 1.2; }
  .holder-role { font-size: 12px; font-weight: 400; letter-spacing: 2.5px; margin-top: 1px; }

  .contact-list { position: absolute; left: 60px; top: 177px; list-style: none; }
  .contact-item { display: flex; align-items: center; height: 40px; margin-bottom: 32px; }
  .contact-icon {
    width: 40px; height: 40px; border-radius: 7px; background: var(--charcoal);
    display: flex; align-items: center; justify-content: center; flex: none;
  }
  .contact-text {
    margin-left: 23px; color: var(--ink); font-size: 13px;
    letter-spacing: 1.6px; line-height: 20px; white-space: nowrap;
  }
</style>
</head>
<body>

<section class="card card-front" aria-label="Card front">
  <svg class="card-shapes" width="720" height="433" viewBox="0 0 720 433">
    <polygon points="334,0 720,0 720,43 378,43" fill="var(--accent-yellow)"/>
    <polygon points="378,392 720,392 720,433 334,433" fill="var(--accent-yellow)"/>
    <defs>
      <linearGradient id="pattern-tone" x1="0" y1="0" x2="1" y2="0">
        <stop offset="0" stop-color="#3a3a3a"/>
        <stop offset="1" stop-color="#474747"/>
      </linearGradient>
    </defs>
    <rect x="465" y="100" width="255" height="158" fill="url(#pattern-tone)" role="img" aria-label="Scattered square pattern"/>
  </svg>
  <div class="brand brand-front">
    <span class="brand-dot"></span>
    <span class="brand-name">Haskell Law</span>
  </div>
  <ul class="practice">
    <li>Civil Litigation · Corporate Law</li>
    <li>Business Governance · Real Estate Law</li>
    <li class="practice-years">25+ Years of Experience</li>
  </ul>
</section>

<section class="card card-back" aria-label="Card back">
  <svg class="card-shapes" width="720" height="433" viewBox="0 0 720 433">
    <polygon points="0,0 488,0 408,84 0,84" fill="var(--charcoal)"/>
  </svg>
  <div class="holder">
    <div class="holder-name">TOBIN HASKELL</div>
    <div class="holder-role">ATTORNEY AT LAW</div>
  </div>

  <ul class="contact-list">
    <li class="contact-item">
      <span class="contact-icon">
        <svg width="22" height="22" viewBox="0 0 24 24" aria-hidden="true">
          <path fill="#fff" d="M6.6 10.8a15.1 15.1 0 0 0 6.6 6.6l2.2-2.2a1 1 0 0 1 1-.25 11.4 11.4 0 0 0 3.6.57 1 1 0 0 1 1 1V20a1 1 0 0 1-1 1A17 17 0 0 1 3 4a1 1 0 0 1 1-1h3.5a1 1 0 0 1 1 1c0 1.250.2 2.450.57 3.57a1 1 0 0 1-.25 1z"/>
        </svg>
      </span>
      <span class="contact-text">+12 555 014 2290<br>+12 555 014 2291</span>
    </li>
    <li class="contact-item">
      <span class="contact-icon">
        <svg width="24" height="24" viewBox="0 0 24 24" fill="none" stroke="#fff" stroke-width="1.6" aria-hidden="true">
          <circle cx="12" cy="12" r="9"/>
          <ellipse cx="12" cy="12" rx="4" ry="9"/>
          <line x1="3" y1="12" x2="21" y2="12"/>
          <path d="M5 7.5h14M5 16.5h14"/>
        </svg>
      </span>
      <span class="contact-text">INFO@HASKELLLAW.COM<br>HASKELLLAW.COM</span>
    </li>
    <li class="contact-item">
      <span class="contact-icon">
        <svg width="20" height="22" viewBox="0 0 24 24" aria-hidden="true">
          <path fill="#fff" d="M12 2a7 7 0 0 0-7 7c0 5.2 7 13 7 13s7-7.8 7-13a7 7 0 0 0-7-7zm0 9.6A2.6 2.6 0 1 1 12 6.4a2.6 2.6 0 0 1 0 5.2z"/>
        </svg>
      </span>
      <span class="contact-text">418 ALDER STREET, SUITE 9<br>PORTLAND, OR 97204</span>
    </li>
  </ul>

  <div class="brand brand-back">
    <span class="brand-dot"></span>
    <span class="brand-name">Haskell Law</span>
  </div>
</section>

</body>
</html>
```